Eco friendly Swedish beauty products sold in aluminum bottles - label design needed

We need help in designing a series of stick on labels for 80 ml (2.7 fl. oz.) aluminum bottles containing beauty products such as soaps, shampoo etc. The diameter of the bottle is 36 mm and the body of the bottles measures approx. 106 mm.
It is important for us that the label has a simplistic and clean feel with few colors (and the right ones!) and that the label helps amplify this product being both better and a more sustainable alternative to many of our plastic bottle competitors. The design and label should communicate the feel of an Eco-friendly, sustainable and modern brand of high quality - and with a Swedish concept.
We are using Montserrat font in our materials. Find attached information of preferred colors, the bottles and one example of our logotype. I am also available on e-mail should further information be needed.

Looking forward and very excited to receive your suggestions.
Note that we are expecting to start selling a series of approximately 10 different products where I will need one "master design" and then only smaller changes for each of the different products.

Target Market(s)

People whom are aware and not only look at price tag. Private and commercial market.

Industry/Entity Type

Beauty

Font styles to use
Other font styles liked:
• Montserrat

Requirements
Must have
• It must give the feel of being both better and a more sustainable alternative to many of our plastic bottle competitors.
Nice to have
• Simplistic. Clean. Clear.
Should not have
• Wrong colors, too complex designs.

```html
<!DOCTYPE html>
<html lang="en">
<head>
<meta charset="UTF-8">
<title>Olive Shampoo Label</title>
<link rel="stylesheet" href="https://fonts.googleapis.com/css2?family=Montserrat:wght@400;500&display=swap">
<style>
  :root {
    --page: #ffffff;
    --label-cream: #fdfdf6;
    --ink: #161616;
    --band-stone: #d9d6c5;
    --band-sage: #aeb393;
    --band-moss: #878e59;
    --band-olive: #6d763a;
    --rule: #6b6b6b;
  }
  * { margin: 0; padding: 0; box-sizing: border-box; }
  html, body {
    width: 1200px;
    height: 848px;
    overflow: hidden;
    background: var(--page);
  }
  .canvas {
    position: relative;
    width: 1200px;
    height: 848px;
    font-family: "Montserrat", sans-serif;
    color: var(--ink);
  }
  .label {
    position: absolute;
    left: 417px;
    top: 192px;
    width: 365px;
    height: 465px;
    display: flex;
  }
  .label__panel {
    position: relative;
    width: 237px;
    height: 100%;
    background: var(--label-cream);
  }
  .label__brand {
    position: absolute;
    left: 27px;
    top: 36px;
    font-size: 14px;
    font-weight: 400;
    letter-spacing: 0.02em;
    white-space: nowrap;
  }
  .label__product {
    position: absolute;
    left: 27px;
    top: 96px;
    font-size: 33px;
    font-weight: 400;
    line-height: 40px;
    letter-spacing: 0.01em;
  }
  .label__volume {
    position: absolute;
    left: 27px;
    top: 377px;
    font-size: 14px;
    font-weight: 400;
    letter-spacing: 0.01em;
  }
  .label__rule {
    position: absolute;
    left: 27px;
    top: 424px;
    width: 182px;
    height: 1px;
    background: var(--rule);
  }
  .label__bands {
    width: 128px;
    height: 100%;
    display: flex;
    flex-direction: column;
  }
  .band { width: 100%; }
  .band--stone { height: 73px; background: var(--band-stone); }
  .band--sage  { height: 117px; background: var(--band-sage); }
  .band--moss  { height: 117px; background: var(--band-moss); }
  .band--olive { flex: 1; background: var(--band-olive); }
</style>
</head>
<body>
  <main class="canvas">
    <section class="label">
      <div class="label__panel">
        <p class="label__brand">Stillwater Botanics</p>
        <h1 class="label__product">OLIVE<br>SHAMPOO</h1>
        <p class="label__volume">2.7 fl. oz | 80 ml</p>
        <div class="label__rule"></div>
      </div>
      <div class="label__bands">
        <div class="band band--stone"></div>
        <div class="band band--sage"></div>
        <div class="band band--moss"></div>
        <div class="band band--olive"></div>
      </div>
    </section>
  </main>
</body>
</html>
```